Large multi-office optometry business opening a Dry Eye Spa and needs sign.

Business name/sign info: Brenwick Dry Eye Institute, (555) 362-4817
Backlit pole sign at office entrance on a very busy street
Sign dimensions: 53" tall x 136.5" wide
State of the art Dry Eye Spa for treatment of all forms of dry eye and ocular surface disease. Also, have aesthetics treatments (IPL, Low Level Light Treatment, etc.)

Target Market(s)

People who are suffering from: dryness, burning, foreign body sensation, itching, fluctuating vision, tired eyes, etc.

Industry/Entity Type

Optometry and aesthetics

Colors
0054AA
0677BA
7BADD7
CADEEF
E8F1F8

Requirements
Must have
• Business name, phone number, subliminal message of relief in a glance or short look.
Nice to have
• Cool, relief, soothing sense.
Should not have
• Too much information or too busy.

```html
<!DOCTYPE html>
<html lang="en">
<head>
<meta charset="utf-8">
<title>Brenwick Dry Eye Institute – Pole Sign</title>
<link href="https://fonts.googleapis.com/css2?family=Roboto+Slab:wght@700&family=Roboto:wght@500&display=swap" rel="stylesheet">
<style>
  :root {
    --backdrop: #adabac;
    --blue-deep: #0c6dbd;
    --blue-bright: #26a3df;
    --photo-white: #f1efec;
    --photo-skin: #e2c2ad;
    --photo-hair: #5a3c2c;
    --photo-tape: #2aa6dc;
    --stripe: #ffffff;
    --text: #ffffff;
  }
  html, body {
    margin: 0;
    width: 1200px;
    height: 1200px;
    overflow: hidden;
    background: var(--backdrop);
  }
  .sign {
    position: absolute;
    left: 115px;
    top: 412px;
    width: 970px;
    height: 375px;
    overflow: hidden;
  }
  .sign-art {
    position: absolute;
    inset: 0;
    width: 100%;
    height: 100%;
  }
  .sign-name {
    position: absolute;
    left: 69px;
    top: 32px;
    margin: 0;
    font-family: "Roboto Slab", "Rockwell", "DejaVu Serif", serif;
    font-weight: 700;
    font-size: 74px;
    line-height: 72px;
    color: var(--text);
  }
  .sign-name span { display: block; white-space: nowrap; }
  .sign-phone {
    position: absolute;
    left: 75px;
    top: 284px;
    margin: 0;
    font-family: "Roboto", Arial, sans-serif;
    font-weight: 500;
    font-size: 39px;
    color: var(--text);
    white-space: nowrap;
  }
</style>
</head>
<body>
  <div class="sign">
    <svg class="sign-art" viewBox="0 0 776 300" preserveAspectRatio="none" xmlns="http://www.w3.org/2000/svg">
      <defs>
        <linearGradient id="panelBlue" x1="0" y1="1" x2="1" y2="0">
          <stop offset="0" stop-color="var(--blue-deep)"/>
          <stop offset="0.6" stop-color="#1580cc"/>
          <stop offset="1" stop-color="var(--blue-bright)"/>
        </linearGradient>
        <radialGradient id="photoTone" cx="0.5" cy="0.5" r="0.65">
          <stop offset="0" stop-color="var(--photo-skin)"/>
          <stop offset="0.35" stop-color="#c9a690"/>
          <stop offset="0.6" stop-color="var(--photo-hair)" stop-opacity="0.75"/>
          <stop offset="1" stop-color="var(--photo-white)"/>
        </radialGradient>
      </defs>
      <rect class="photo-base" x="300" y="0" width="476" height="300" fill="var(--photo-white)"/>
      <rect class="treatment-photo" x="300" y="0" width="476" height="300" fill="url(#photoTone)" role="img" aria-label="Photo of a woman lying relaxed on a treatment bed, blue therapy tape on her cheek, receiving a soothing dry eye spa treatment"/>
      <g class="photo-stripes" fill="var(--stripe)">
        <polygon points="553,0 565,0 430,300 418,300"/>
        <polygon points="612,0 625,0 490,300 477,300"/>
        <polygon points="668,0 681,0 546,300 533,300"/>
        <polygon points="722,0 735,0 600,300 587,300"/>
        <polygon points="770,0 776,0 776,6 655,300 642,300"/>
      </g>
      <polygon class="brand-panel" points="0,0 493,0 335,300 0,300" fill="url(#panelBlue)"/>
    </svg>
    <h1 class="sign-name">
      <span>Brenwick</span>
      <span>DRY EYE</span>
      <span>Institute</span>
    </h1>
    <p class="sign-phone">(555) 362-4817</p>
  </div>
</body>
</html>
```